Consumer and commercial IOT solutions (Internet Of Things)

We are a startup and are looking for business cards with logo. The logo will appear on all of our media as well as our ecommerce site and social sites that have yet to be developed. We want to present a fresh face on a high tech company that innovates at every turn. You can read about our solutions on our information only web site www.plendacore.net - We have some wording we would like used on our business cards but there is no place for this except for here. The company name is "RM Industrial IOT" I have some samples of logos I am interested in seeing but I will let your team make the initial presentations

```html
<!DOCTYPE html>
<html lang="en">
<head>
<meta charset="utf-8">
<title>Plendacore – Business Card</title>
<link rel="stylesheet" href="https://fonts.googleapis.com/css2?family=Open+Sans:wght@400;600&display=swap">
<style>
  :root {
    --backdrop: #e9ecf0;
    --card: #ffffff;
    --ink-navy: #1f2a44;
    --ink-text: #2b2f36;
    --accent-blue: #3f86c8;
    --icon-blue: #4a8fd0;
  }
  * { box-sizing: border-box; margin: 0; padding: 0; }
  html, body {
    width: 1200px;
    height: 786px;
    overflow: hidden;
    background: var(--backdrop);
  }
  .business-card {
    position: absolute;
    left: 100px;
    top: 107px;
    width: 1000px;
    height: 571px;
    background: var(--card);
    box-shadow: 0 10px 30px rgba(20, 30, 50, 0.14);
    font-family: "Open Sans", sans-serif;
    color: var(--ink-text);
  }
  .brand {
    position: absolute;
    left: 66px;
    top: 70px;
    width: 360px;
    display: flex;
    flex-direction: column;
    align-items: center;
  }
  .brand-square {
    width: 120px;
    height: 120px;
    background: var(--accent-blue);
    margin-bottom: 34px;
  }
  .brand-name {
    font-family: "Open Sans", sans-serif;
    font-weight: 600;
    font-size: 50px;
    color: var(--ink-navy);
    white-space: nowrap;
  }
  .contact {
    position: absolute;
    left: 680px;
    top: 200px;
  }
  .contact-name {
    font-size: 36px;
    color: var(--ink-navy);
    letter-spacing: 0.5px;
    line-height: 1.1;
  }
  .contact-role {
    font-size: 22px;
    color: var(--ink-text);
    margin-bottom: 38px;
  }
  .contact-lines { list-style: none; margin-bottom: 32px; }
  .contact-lines li {
    display: flex;
    align-items: center;
    gap: 14px;
    font-size: 23px;
    line-height: 1.45;
  }
  .contact-lines svg { width: 20px; height: 20px; flex: none; }
  .address { font-size: 22px; line-height: 1.45; }
  .accent-bar {
    position: absolute;
    left: 680px;
    bottom: 0;
    width: 270px;
    height: 7px;
    background: var(--accent-blue);
  }
</style>
</head>
<body>
  <div class="business-card">
    <div class="brand">
      <div class="brand-square"></div>
      <div class="brand-name">Plendacore</div>
    </div>

    <div class="contact">
      <div class="contact-name">EVAN MARLOW</div>
      <div class="contact-role">Manager</div>
      <ul class="contact-lines">
        <li>
          <svg viewBox="0 0 20 20" fill="none" stroke="var(--icon-blue)" stroke-width="1.6" stroke-linejoin="round">
            <path d="M5 2.5l3 3.5-1.8 2a10 10 0 0 0 5.8 5.8l2-1.8 3.5 3-1.8 2.5C9.5 17.5 2.5 10.5 2.5 4.3z"/>
          </svg>
          <span>000-000-0000</span>
        </li>
        <li>
          <svg viewBox="0 0 20 20" fill="none" stroke="var(--icon-blue)" stroke-width="1.6" stroke-linejoin="round">
            <rect x="2" y="4.5" width="16" height="11"/>
            <path d="M2 4.5l8 6.5 8-6.5"/>
          </svg>
          <span>evan@plendacore.net</span>
        </li>
        <li>
          <svg viewBox="0 0 20 20" fill="none" stroke="var(--icon-blue)" stroke-width="1.5">
            <circle cx="10" cy="10" r="7.5"/>
            <ellipse cx="10" cy="10" rx="3.2" ry="7.5"/>
            <path d="M2.5 10h15M3.8 6h12.4M3.8 14h12.4"/>
          </svg>
          <span>www.plendacore.net</span>
        </li>
      </ul>
      <div class="address">
        0000 Main St.<br>
        Alder Bay, CA 00000
      </div>
    </div>

    <div class="accent-bar"></div>
  </div>
</body>
</html>
```